Church Bulletin Ad (see attached sample)

Create a New Church Bulletin Ad. I have attached some samples of what we would like to have in the ad. (1) Marrowfield Realty Thorne Logo (2) Headshot (3) Lena Vasko & Greta Vasko, Real Estate Team (4) Phone number (5) Email address (6) St Aldwin Parishioners for over 40 Years. We would like for the ad to be clean and modern. NO OTHER IMAGES besides headshots and Marrowfield Realty Thorne Logo.

Target Market(s)

Church community

Industry/Entity Type

Real Estate

Font styles to use
Sans Serif
Other font styles liked:
• Modern Font

Colors
0054AA
0677BA
7BADD7
CADEEF
E8F1F8

Requirements
Must have
• Marrowfield Realty Thorne Logo; Headshot; Ad size is 4.5"x1.62"

```html
<!DOCTYPE html>
<html lang="en">
<head>
<meta charset="utf-8">
<title>Lena Vasko &amp; Greta Vasko Real Estate Team – Bulletin Ad</title>
<link rel="stylesheet" href="https://fonts.googleapis.com/css2?family=Bebas+Neue&family=Figtree:wght@800&family=Roboto:ital,wght@1,700&family=Roboto+Condensed:ital,wght@1,700&display=swap">
<style>
  :root {
    --page-bg: #666666;
    --navy: #0b3159;
    --logo-navy: #0d3a66;
    --ink: #111111;
    --white: #ffffff;
    --paper-light: #ffffff;
    --paper-shade: #eef0f2;
    --photo-dark: #3a3532;
    --photo-mid: #8c7f78;
    --photo-light: #e9e6e3;
  }
  * { margin: 0; padding: 0; box-sizing: border-box; }
  html, body {
    width: 1200px;
    height: 1200px;
    overflow: hidden;
    background: var(--page-bg);
  }
  .ad {
    position: absolute;
    left: 171px;
    top: 417px;
    width: 861px;
    height: 366px;
    overflow: hidden;
    background: linear-gradient(160deg, var(--paper-light) 0%, var(--paper-shade) 45%, var(--paper-light) 70%);
  }
  .headline {
    position: absolute;
    left: 33px;
    top: 24px;
    font-family: "Bebas Neue", sans-serif;
    font-size: 61px;
    line-height: 1;
    letter-spacing: 0.4px;
    color: var(--navy);
    white-space: nowrap;
  }
  .brand-box {
    position: absolute;
    left: 696px;
    top: 28px;
    width: 129px;
    height: 117px;
    background: var(--logo-navy);
    display: flex;
    align-items: center;
    justify-content: center;
    text-align: center;
  }
  .brand-name {
    font-family: "Figtree", sans-serif;
    font-weight: 800;
    font-size: 13px;
    line-height: 1.25;
    letter-spacing: 0.5px;
    color: var(--white);
  }
  .headshot {
    position: absolute;
    top: 93px;
    height: 273px;
  }
  .headshot--lena {
    left: 0;
    width: 225px;
    background: linear-gradient(180deg, var(--photo-light) 0%, var(--photo-mid) 45%, var(--photo-dark) 100%);
  }
  .headshot--greta {
    left: 225px;
    width: 236px;
    background: linear-gradient(180deg, var(--photo-light) 0%, var(--photo-mid) 45%, var(--photo-dark) 100%);
  }
  .team {
    position: absolute;
    right: 38px;
    top: 164px;
    text-align: right;
    font-family: "Figtree", sans-serif;
    font-weight: 800;
    font-size: 27px;
    line-height: 37px;
    color: var(--ink);
    white-space: nowrap;
  }
  .contact {
    position: absolute;
    right: 36px;
    display: flex;
    align-items: center;
    gap: 5px;
    font-family: "Roboto", sans-serif;
    font-style: italic;
    font-weight: 700;
    color: var(--ink);
    white-space: nowrap;
  }
  .contact--phone { top: 250px; font-size: 20px; }
  .contact--email { top: 284px; font-size: 19px; }
  .contact-icon { width: 26px; height: 26px; flex: none; }
  .tagline-band {
    position: absolute;
    left: 461px;
    top: 320px;
    width: 400px;
    height: 46px;
    background: var(--navy);
    display: flex;
    align-items: center;
    justify-content: flex-end;
    padding-right: 35px;
  }
  .tagline {
    font-family: "Roboto Condensed", sans-serif;
    font-style: italic;
    font-weight: 700;
    font-size: 19px;
    color: var(--white);
    white-space: nowrap;
  }
</style>
</head>
<body>
  <section class="ad">
    <h1 class="headline">Energy Excellence Experience</h1>

    <div class="brand-box">
      <span class="brand-name">MARROWFIELD<br>REALTY<br>THORNE</span>
    </div>

    <div class="headshot headshot--lena" role="img" aria-label="Headshot of Lena Vasko"></div>
    <div class="headshot headshot--greta" role="img" aria-label="Headshot of Greta Vasko"></div>

    <p class="team">Lena Vasko &amp; Greta Vasko<br>Real Estate Team</p>

    <p class="contact contact--phone">
      (206) 555-0142
      <svg class="contact-icon" viewBox="0 0 26 26" aria-hidden="true">
        <circle cx="13" cy="13" r="11.5" fill="none" stroke="#0b3159" stroke-width="1.8"/>
        <path d="M9 7.5c.6-.5 1.3-.4 1.7.2l1.1 1.8c.3.5.2 1.1-.2 1.4l-.9.7c.6 1.5 1.8 2.8 3.3 3.5l.7-.9c.4-.4 1-.5 1.4-.2l1.8 1.1c.6.4.7 1.1.2 1.7l-.8.9c-.6.6-1.5.8-2.3.5-3.2-1.2-5.6-3.7-6.8-6.9-.3-.8-.1-1.7.5-2.3z" fill="#0b3159"/>
        <path d="M14.5 8.2a4 4 0 0 1 3.3 3.3M14.8 5.8a6.4 6.4 0 0 1 5.4 5.4" fill="none" stroke="#0b3159" stroke-width="1.2" stroke-linecap="round"/>
      </svg>
    </p>

    <p class="contact contact--email">
      VaskoLane Team@MRThorne.com
      <svg class="contact-icon" viewBox="0 0 26 26" aria-hidden="true">
        <circle cx="13" cy="13" r="11.5" fill="none" stroke="#0b3159" stroke-width="1.8"/>
        <rect x="7" y="9" width="12" height="8.5" rx="1" fill="#0b3159"/>
        <path d="M7.5 9.6l5.5 4.2 5.5-4.2" fill="none" stroke="#ffffff" stroke-width="1.1"/>
      </svg>
    </p>

    <div class="tagline-band">
      <p class="tagline">St Aldwin Parishioners for over 40 Years.</p>
    </div>
  </section>
</body>
</html>
```